Velvet Harbour - R&B Band in Sydney Requires new Business Cards

We're a 6 piece R&B Soul band in Sydney called Velvet Harbour that requires new promotional material including Business Cards.

We are very well known around Sydney and have a resident venue gig at the Marlowe Grand Sydney hotel. We play predominantly old & new school R&B hits.

Our logo is attached, colours are Brown & yellow.
Initial idea was to get sugar packets made up with our logo and contact details.

```html
<!DOCTYPE html>
<html lang="en">
<head>
<meta charset="utf-8">
<title>Velvet Harbour – Business Cards</title>
<link href="https://fonts.googleapis.com/css2?family=Open+Sans:wght@400;700&display=swap" rel="stylesheet">
<style>
  :root {
    --yellow: #e9ec1f;
    --yellow-light: #f3f25a;
    --brown: #3a2a1f;
    --brown-dark: #2b1f17;
    --backdrop: #d9d4cc;
  }
  * { margin: 0; padding: 0; box-sizing: border-box; }
  html, body {
    width: 1200px; height: 1023px; overflow: hidden;
    background: var(--backdrop);
    font-family: "Open Sans", Arial, sans-serif;
  }
  .sheet {
    width: 1200px; height: 1023px;
    display: flex; align-items: center; justify-content: center; gap: 60px;
  }
  .card {
    width: 520px; height: 316px; border-radius: 18px;
    position: relative; overflow: hidden;
    box-shadow: 0 6px 18px rgba(0,0,0,.18);
  }
  .card--front {
    background: linear-gradient(160deg, var(--yellow-light), var(--yellow));
    color: var(--brown);
  }
  .contact {
    position: absolute; top: 22px; right: 30px; text-align: right;
    font-size: 13px; line-height: 1.45;
  }
  .contact__name { font-size: 21px; font-weight: 700; letter-spacing: .5px; line-height: 1.2; }
  .contact__role { font-size: 12px; }
  .contact__company { margin-bottom: 8px; }
  .contact__group { margin-bottom: 8px; }
  .contact__group:last-child { margin-bottom: 0; }
  .mic-art {
    position: absolute; left: 0; right: 0; bottom: 0; height: 56px;
    background: linear-gradient(180deg, #6b5640, var(--brown));
  }
  .card--back {
    background: linear-gradient(160deg, #4a3628, var(--brown-dark));
    display: flex; align-items: center; justify-content: center;
  }
  .wordmark {
    color: var(--yellow); font-weight: 700; font-size: 46px;
    letter-spacing: 2px; text-transform: uppercase;
    display: flex; align-items: center; gap: 16px;
  }
  .wordmark__dot {
    width: 22px; height: 22px; border-radius: 50%; background: var(--yellow);
  }
</style>
</head>
<body>
<main class="sheet">
  <section class="card card--front">
    <div class="contact">
      <div class="contact__name">RAFE CASTELLANO</div>
      <div class="contact__role">Director</div>
      <div class="contact__company">Velvet Harbour Entertainment Pty Ltd</div>
      <div class="contact__group">
        +61 400 123 456<br>
        info@velvetharbourmusic.com.au<br>
        www.velvetharbourmusic.com.au
      </div>
      <div class="contact__group">
        www.velvetharbourmusic.com.au/live<br>
        www.velvetharbourmusic.com.au/news<br>
        www.velvetharbourmusic.com.au/gallery
      </div>
    </div>
    <div class="mic-art" role="img" aria-label="Brown illustration of a vintage stage microphone"></div>
  </section>

  <section class="card card--back">
    <div class="wordmark"><span class="wordmark__dot"></span>Velvet Harbour</div>
  </section>
</main>
</body>
</html>
```